Responsive OnePage Design for recruitment company

Norvanta is a modern company that sources interim people for its customers. Mostly developers, scrum master, project managers and designers. In this website we want to tell something about us, about how we work, our customers and we want our candidates be able to subscribe. The subscription form should be several fields (name, surname, email address, phone number and the possibility to upload your resume.We want it to fit into a existing wordpress plugin. We also want a listing of our job opportunities. The listing should be designed in a clear readable overview and if you click on the job you should get the details and be able to respond quickly by filling in you name, surname, email address, rate, phone number and upload your resume. We want this to be a standard configurable plugin. It should be easy to fill in the jobs in Wordpress by our administrator. We want a fresh, modern and cool design. It should be a responsive onepage design. If you click on a listed job you should stay on the same page. Our logo is added.

Target Market(s)

recruitment

Industry/Entity Type

Recruitment

Font styles to use
Sans Serif

Colors

Designer to choose colors to be used in the design.

Requirements
Must have
• Onepage design
• listing of job opportunities
• subscription forms
• be responsive

```html
<!DOCTYPE html>
<html lang="en">
<head>
<meta charset="utf-8">
<title>Norvanta — One Page</title>
<link href="https://fonts.googleapis.com/css2?family=Montserrat:wght@500;600&family=Roboto:ital,wght@0,400;0,500;0,700;1,400&display=swap" rel="stylesheet">
<style>
:root{
  --blue:#0b6fbd;
  --blue-dark:#0a5a9a;
  --ink:#2e2e2e;
  --muted:#8a8a8a;
  --grey-btn:#5a5a5a;
  --footer:#595959;
  --board:#e6e6e6;
  --card:#ffffff;
  --soft:#f4f5f7;
}
*{box-sizing:border-box;margin:0;padding:0}
html,body{width:817px;height:1200px;overflow:hidden;background:var(--board);font-family:"Roboto",Arial,sans-serif;color:var(--ink)}
.page{position:absolute;background:#fff;overflow:hidden}
.desktop{left:118px;top:24px;width:368px;height:1146px}
.mobile{left:528px;top:36px;width:125px;height:1116px}
.logo{font-family:"Montserrat",Arial,sans-serif;font-weight:600;color:var(--blue);letter-spacing:2.4px;text-transform:uppercase}
.btn{display:inline-flex;align-items:center;justify-content:center;color:#fff;font-weight:700;text-transform:uppercase;white-space:nowrap}
.btn-blue{background:var(--blue)}
.btn-grey{background:var(--grey-btn)}
.photo{display:block}
.hero-photo{background:linear-gradient(180deg,#dfe6ee 0%,#c9d3de 55%,#eef1f5 100%)}
.office-photo{background:linear-gradient(120deg,#c9cfd6,#e9ecef 45%,#7d8794)}
.desk-photo{background:linear-gradient(120deg,#6f5a48,#b99a7c 50%,#d8d2c8)}
.avatar{border-radius:50%;border:2px solid var(--blue);background:linear-gradient(160deg,#d9c3ad,#8c95a3)}
.blue-band{background:var(--blue);color:#fff}

/* ---------- desktop ---------- */
.d-header{height:22px;display:flex;align-items:center;justify-content:space-between;padding:0 12px}
.d-header .logo{font-size:8.5px;letter-spacing:2.8px}
.burger{width:8px;height:6px;border-top:1px solid #444;border-bottom:1px solid #444;position:relative}
.burger::after{content:"";position:absolute;left:0;right:0;top:2px;border-top:1px solid #444}
.account{font-size:3.6px;color:var(--muted)}
.account b{color:var(--blue);font-weight:400}
.d-hero{height:190px;position:relative}
.d-hero .photo{position:absolute;inset:0}
.hero-copy{position:absolute;left:0;right:0;top:82px;text-align:center}
.hero-copy h1{font-size:21.5px;font-weight:700;color:var(--blue);line-height:1}
.hero-copy p{font-size:11.5px;font-weight:500;color:var(--ink);line-height:1.15}
.d-search{height:41px;padding:8px 13px 0}
.search-row{display:flex;gap:3px}
.field{background:#fff;height:14px;font-size:3.6px;font-style:italic;color:#aaa;display:flex;align-items:center;padding:0 5px}
.search-go{width:20px;height:14px;background:var(--blue-dark);display:flex;align-items:center;justify-content:center;margin-left:2px}
.browse{font-size:3.6px;font-style:italic;margin-top:4px}
.browse span{border:.5px solid #fff;padding:0 3px;margin-left:2px}
.d-jobs{height:253px;padding:18px 28px 0}
.section-title{font-size:9.5px;font-weight:500;text-transform:uppercase;color:var(--ink)}
.section-title em{font-style:normal;color:var(--blue)}
.job-list{margin-top:11px;display:flex;flex-direction:column;gap:6px}
.job{height:52px;display:flex;background:var(--card);box-shadow:0 0 3px rgba(0,0,0,.14)}
.job-info{flex:1;padding:9px 11px}
.job-info h3{font-size:8.5px;font-weight:500;color:var(--blue);line-height:1.1}
.job-info .role{font-size:5.2px;color:#666;margin-top:1px}
.job-meta{display:flex;gap:14px;font-size:3.2px;color:#999;margin-top:10px;white-space:nowrap}
.job-actions{width:82px;background:var(--soft);display:flex;flex-direction:column;align-items:center;justify-content:center;gap:3px}
.job-actions .btn{width:50px;height:12px;font-size:3.6px}
.view-all{display:flex;justify-content:center;margin-top:14px}
.view-all .btn{width:51px;height:13px;font-size:3.6px}
.d-about{height:103px;display:flex}
.about-copy{width:184px;padding:25px 13px 0}
.about-copy h2{font-size:8.5px;font-weight:500}
.about-copy p{font-size:3.4px;line-height:1.35;margin-top:8px}
.about-copy .btn{width:50px;height:12px;font-size:3.4px;margin-top:8px}
.d-about .photo{flex:1}
.d-how{height:142px;padding-top:27px;text-align:center}
.steps{display:flex;margin-top:18px;padding:0 16px}
.step{flex:1;position:relative;padding:0 8px}
.step+.step::before{content:"";position:absolute;left:-4px;top:-4px;width:14px;height:48px;border-right:1px solid #eee;transform:skewX(12deg)}
.step svg{width:18px;height:18px}
.step h4{font-size:8.8px;font-weight:700;color:var(--blue);margin-top:4px}
.step p{font-size:3.4px;color:#777;line-height:1.3;margin-top:1px}
.d-subscribe{height:129px;display:flex}
.d-subscribe .photo{width:184px}
.sub-form{flex:1;padding:13px 28px 0 19px}
.sub-form h2{font-size:8.5px;font-weight:500;letter-spacing:1.8px;text-align:center;text-transform:uppercase}
.grid2{display:grid;grid-template-columns:1fr 1fr;gap:3px;margin-top:8px}
.input{height:13px;border:.6px solid rgba(255,255,255,.6);font-size:3.4px;font-style:italic;display:flex;align-items:center;padding:0 4px}
.textarea{height:32px;border:.6px solid rgba(255,255,255,.6);font-size:3.4px;font-style:italic;padding:3px 4px;margin-top:3px;position:relative}
.upload{position:absolute;right:4px;bottom:4px;background:#f2f2f2;color:#444;font-style:normal;font-size:2.6px;padding:1px 3px}
.sub-form .btn{width:50px;height:12px;font-size:3.4px;margin-top:5px}
.d-cands{height:155px;padding-top:24px;text-align:center}
.d-cands .section-title{letter-spacing:1.4px}
.cand-row{display:flex;align-items:flex-start;justify-content:center;gap:10px;margin-top:16px;position:relative;padding:0 25px}
.arrow{position:absolute;top:16px;width:10px;height:10px;border:.7px solid #888;border-radius:50%;display:flex;align-items:center;justify-content:center}
.arrow.next{right:14px;border-color:var(--blue)}
.arrow.prev{left:14px}
.cand{width:42px}
.cand .avatar{width:42px;height:42px;margin:0 auto}
.cand b{display:block;font-size:3.8px;font-weight:500;margin-top:8px}
.cand i{display:block;font-size:3.4px;color:var(--blue);font-style:normal}
.d-cands .btn{width:60px;height:13px;font-size:3.6px;margin-top:17px}
.d-footer{height:111px;background:var(--footer);color:#e5e5e5;padding:18px 12px 0}
.foot-cols{display:flex}
.foot-brand{width:110px}
.foot-brand .logo{color:#fff;font-size:6.5px;letter-spacing:1.8px}
.foot-brand p{font-size:3.4px;line-height:1.3;margin-top:10px}
.socials{display:flex;gap:6px;margin-top:3px}
.socials span{width:4px;height:4px;border-radius:50%;background:#fff}
.foot-col{width:75px;font-size:3.4px;line-height:1.35}
.foot-col h5{font-size:9px;font-weight:500;color:#fff;margin-bottom:4px}
.mini{height:8px;border:.5px solid #ccc;font-size:2.8px;font-style:italic;padding:1px 3px}
.foot-bottom{display:flex;justify-content:space-between;border-top:.5px solid #888;margin-top:15px;padding-top:7px;font-size:3px}

/* ---------- mobile ---------- */
.m-header{height:16px;display:flex;align-items:center;justify-content:space-between;padding:0 5px}
.m-header .logo{font-size:5.2px;letter-spacing:1.3px}
.m-header .burger{width:5px;height:4px}
.m-header .burger::after{top:1.2px}
.m-header .account{font-size:2.2px}
.m-hero{height:116px;position:relative}
.m-hero .photo{position:absolute;inset:0}
.m-hero .hero-copy{top:50px}
.m-hero h1{font-size:13px}
.m-hero p{font-size:6.5px}
.m-search{height:37px;padding:3px 4px 0}
.m-search .field{height:7px;font-size:2.2px;margin-bottom:2px}
.m-search .browse{font-size:2.2px;margin-top:0}
.m-search .search-go{width:10px;height:7px;margin:0 0 0 auto}
.m-jobs{height:230px;padding:8px 5px 0}
.m-jobs .section-title{font-size:5px}
.m-job{height:61px;box-shadow:0 0 2px rgba(0,0,0,.16);margin-top:3px;padding:5px 8px 0;background:#fff}
.m-job:first-of-type{margin-top:8px}
.m-job h3{font-size:4.5px;font-weight:500;color:var(--blue);line-height:1.2}
.m-job .role{font-size:2.6px;color:#666;line-height:1.3}
.m-job .job-meta{font-size:2px;gap:6px;margin-top:6px}
.m-job .acts{display:flex;flex-direction:column;align-items:center;gap:3px;margin-top:12px}
.m-job .btn{width:30px;height:6px;font-size:2.2px}
.m-jobs .view-all{margin-top:10px}
.m-jobs .view-all .btn{width:30px;height:7px;font-size:2.2px}
.m-about{height:62px;text-align:center;padding:17px 10px 0}
.m-about h2{font-size:4.5px;font-weight:500}
.m-about p{font-size:2.2px;line-height:1.3;margin-top:3px}
.m-about .btn{width:30px;height:6px;font-size:2.2px;margin-top:4px}
.m-photo{height:70px}
.m-how{height:260px;text-align:center;padding-top:10px}
.m-how .section-title{font-size:4.5px}
.m-step{height:49px;padding-top:9px}
.m-step svg{width:10px;height:10px}
.m-step h4{font-size:4.5px;color:var(--blue);font-weight:700}
.m-step p{font-size:2px;color:#888;line-height:1.3;width:34px;margin:0 auto}
.m-sub-photo{height:75px}
.m-subscribe{height:81px;padding:7px 26px 0}
.m-subscribe h2{font-size:5px;font-weight:500;letter-spacing:1px;text-align:center}
.m-subscribe .grid2{gap:2px;margin-top:5px}
.m-subscribe .input{height:7px;font-size:2px;padding:0 2px}
.m-subscribe .textarea{height:20px;font-size:2px;margin-top:2px;padding:1px 2px}
.m-subscribe .upload{font-size:1.6px}
.m-subscribe .btn{width:20px;height:5px;font-size:1.8px;margin-top:3px}
.m-cands{height:80px;text-align:center;padding-top:9px}
.m-cands .section-title{font-size:5px}
.m-cands .cand-row{gap:6px;margin-top:7px;padding:0}
.m-cands .arrow{top:10px;width:6px;height:6px}
.m-cands .arrow.prev{left:5px}.m-cands .arrow.next{right:5px}
.m-cands .cand{width:26px}
.m-cands .avatar{width:26px;height:26px;border-width:1.3px}
.m-cands .cand b{font-size:2.2px;margin-top:3px}
.m-cands .cand i{font-size:2px}
.m-cands .btn{width:32px;height:6px;font-size:2px;margin-top:6px}
.m-footer{height:90px;background:var(--footer);color:#ddd;padding:10px 6px 0}
.m-footer .logo{color:#fff;font-size:3.8px;letter-spacing:1px}
.m-footer p{font-size:2.2px;line-height:1.3;margin-top:4px}
.m-footer .socials{gap:4px;margin-top:2px}
.m-footer .socials span{width:2.5px;height:2.5px}
.m-links{margin-top:10px}
.m-links div{display:flex;justify-content:space-between;align-items:center;font-size:4.2px;color:#fff;line-height:1.4}
.m-links i{width:4px;height:4px;border:.5px solid #ddd;border-radius:50%}
.m-copy{font-size:1.8px;text-align:center;border-top:.4px solid #888;margin-top:12px;padding-top:5px;line-height:1.5}
</style>
</head>
<body>

<svg width="0" height="0" style="position:absolute">
  <defs>
    <symbol id="i-connect" viewBox="0 0 24 24"><g fill="none" stroke="#444" stroke-width="1.2"><circle cx="12" cy="12" r="4"/><circle cx="12" cy="12" r="9"/><path d="M12 3v5M12 16v5M3 12h5M16 12h5"/></g></symbol>
    <symbol id="i-analyze" viewBox="0 0 24 24"><g fill="none" stroke="#444" stroke-width="1.2"><rect x="3" y="3" width="13" height="18"/><path d="M6 8h7M6 11h5"/><circle cx="17" cy="15" r="4"/></g></symbol>
    <symbol id="i-search" viewBox="0 0 24 24"><g fill="none" stroke="#444" stroke-width="1.4"><circle cx="10" cy="10" r="6"/><path d="M14.5 14.5L20 20"/></g></symbol>
    <symbol id="i-rank" viewBox="0 0 24 24"><g fill="none" stroke="#444" stroke-width="1.2"><circle cx="12" cy="9" r="6"/><circle cx="12" cy="9" r="3"/><path d="M8 14l-2 7 6-3 6 3-2-7"/></g></symbol>
    <symbol id="i-deliver" viewBox="0 0 24 24"><g fill="none" stroke="#444" stroke-width="1.2"><rect x="3" y="7" width="18" height="13"/><path d="M3 7l9 7 9-7M7 4h10v5"/></g></symbol>
    <symbol id="i-lens" viewBox="0 0 24 24"><g fill="none" stroke="#fff" stroke-width="2.4"><circle cx="10" cy="10" r="6"/><path d="M14.5 14.5L20 20"/></g></symbol>
  </defs>
</svg>

<!-- Desktop layout -->
<main class="page desktop">
  <header class="d-header">
    <span class="burger"></span>
    <span class="logo">Norvanta</span>
    <span class="account">Login | <b>Register</b></span>
  </header>

  <section class="d-hero">
    <div class="photo hero-photo" role="img" aria-label="Businessman in a suit facing a city skyline"></div>
    <div class="hero-copy"><h1>YOUR GATEWAY</h1><p>TO A BETTER FUTURE</p></div>
  </section>

  <section class="d-search blue-band">
    <div class="search-row">
      <div class="field" style="width:159px">Job title, Keywords or Company name</div>
      <div class="field" style="width:155px">City, Province or region</div>
      <div class="search-go"><svg width="7" height="7"><use href="#i-lens"/></svg></div>
    </div>
    <p class="browse">Or browse jobs offer by <span>Category</span></p>
  </section>

  <section class="d-jobs">
    <h2 class="section-title">Feature <em>Jobs</em></h2>
    <div class="job-list">
      <article class="job">
        <div class="job-info"><h3>Job Title</h3><p class="role">Scrum Master</p>
          <div class="job-meta"><span>Part-Time</span><span>China</span><span>Up to $ 55000+Commision</span><span>8:00 AM to 5:00 PM</span></div></div>
        <div class="job-actions"><span class="btn btn-grey">Full Detail</span><span class="btn btn-blue">Quick Inquiry</span></div>
      </article>
      <article class="job">
        <div class="job-info"><h3>Job Title</h3><p class="role">Project Manager</p>
          <div class="job-meta"><span>Full-Time</span><span>USA</span><span>Up to $ 55000+Commision</span><span>8:00 AM to 5:00 PM</span></div></div>
        <div class="job-actions"><span class="btn btn-blue">Full Detail</span><span class="btn btn-blue">Quick Inquiry</span></div>
      </article>
      <article class="job">
        <div class="job-info"><h3>Job Title</h3><p class="role">Designer</p>
          <div class="job-meta"><span>Full-Time</span><span>USA</span><span>Up to $ 30000+Commision</span><span>8:00 AM to 5:00 PM</span></div></div>
        <div class="job-actions"><span class="btn btn-blue">Full Detail</span><span class="btn btn-blue">Quick Inquiry</span></div>
      </article>
    </div>
    <div class="view-all"><span class="btn btn-blue">View All Jobs</span></div>
  </section>

  <section class="d-about">
    <div class="about-copy blue-band">
      <h2>ABOUT US</h2>
      <p>Lorem Ipsum is simply dummy text of the printing and typesetting industry. Lorem Ipsum has been the industry's standard dummy text ever since the 1500s, when an unknown printer took a galley of type and scrambled it to make a type specimen book.</p>
      <span class="btn btn-grey">Read More</span>
    </div>
    <div class="photo office-photo" role="img" aria-label="Recruiter shaking hands with a smiling candidate in an office"></div>
  </section>

  <section class="d-how">
    <h2 class="section-title">How we <em>work?</em></h2>
    <div class="steps">
      <div class="step"><svg><use href="#i-connect"/></svg><h4>Connect</h4><p>Lorem Ipsum is simply dummy text of the printing and typesetting industry.</p></div>
      <div class="step"><svg><use href="#i-analyze"/></svg><h4>Analyze</h4><p>Lorem Ipsum is simply dummy text of the printing and typesetting industry.</p></div>
      <div class="step"><svg><use href="#i-search"/></svg><h4>Search</h4><p>Lorem Ipsum is simply dummy text of the printing and typesetting industry.</p></div>
      <div class="step"><svg><use href="#i-rank"/></svg><h4>Rank</h4><p>Lorem Ipsum is simply dummy text of the printing and typesetting industry.</p></div>
      <div class="step"><svg><use href="#i-deliver"/></svg><h4>Deliver</h4><p>Lorem Ipsum is simply dummy text of the printing and typesetting industry.</p></div>
    </div>
  </section>

  <section class="d-subscribe">
    <div class="photo desk-photo" role="img" aria-label="Young woman working on a laptop at a wooden desk"></div>
    <form class="sub-form blue-band">
      <h2>Subscribe</h2>
      <div class="grid2">
        <div class="input">Your name</div><div class="input">Your surname</div>
        <div class="input">Email address</div><div class="input">Phone#</div>
      </div>
      <div class="textarea">Message<span class="upload">Upload Resume ⤓</span></div>
      <span class="btn btn-grey">Subscribe</span>
    </form>
  </section>

  <section class="d-cands">
    <h2 class="section-title">Feature <em>Candidates</em></h2>
    <div class="cand-row">
      <span class="arrow prev"><svg width="5" height="5" viewBox="0 0 10 10"><path d="M6 2L3 5l3 3M3 5h6" fill="none" stroke="#888"/></svg></span>
      <div class="cand"><div class="avatar" role="img" aria-label="Candidate portrait"></div><b>Liam Porter</b><i>Designation</i></div>
      <div class="cand"><div class="avatar" role="img" aria-label="Candidate portrait"></div><b>Noah Grant</b><i>Designation</i></div>
      <div class="cand"><div class="avatar" role="img" aria-label="Candidate portrait"></div><b>Ethan Cole</b><i>Designation</i></div>
      <div class="cand"><div class="avatar" role="img" aria-label="Candidate portrait"></div><b>Mason Reed</b><i>Designation</i></div>
      <div class="cand"><div class="avatar" role="img" aria-label="Candidate portrait"></div><b>Lucas Hale</b><i>Designation</i></div>
      <div class="cand"><div class="avatar" role="img" aria-label="Candidate portrait"></div><b>Owen Blake</b><i>Designation</i></div>
      <span class="arrow next"><svg width="5" height="5" viewBox="0 0 10 10"><path d="M4 2l3 3-3 3M7 5H1" fill="none" stroke="#0b6fbd"/></svg></span>
    </div>
    <span class="btn btn-blue">View All Candidates</span>
  </section>

  <footer class="d-footer">
    <div class="foot-cols">
      <div class="foot-brand">
        <span class="logo">Norvanta</span>
        <p>Lorem Ipsum is simply dummy text of the printing and typesetting industry. Lorem Ipsum has been the industry's standard dummy text ever since the 1500s.</p>
        <div class="socials"><span></span><span></span><span></span><span></span></div>
      </div>
      <div class="foot-col" style="margin-left:2px"><h5>Quick Links</h5>Home<br>About us<br>How We Work<br>Jobs<br>Candidates<br>Subscribe<br>Contact us</div>
      <div class="foot-col"><h5>Useful Info..</h5>(+012) 555 019 9<br>(+012) 555 019 9<br>(+012) 555 019 9<br>info@norvanta.com<br>48 Elm Street<br>Salem, MA 01970</div>
      <div class="foot-col" style="width:68px"><h5>Contact us</h5>
        <div class="grid2" style="margin-top:0;gap:1px"><div class="mini">Full Name</div><div class="mini">Email</div></div>
        <div class="mini" style="height:14px;margin-top:1px">Message</div>
        <span class="btn btn-blue" style="font-size:2.6px;padding:1px 4px;margin-top:3px">Submit Now</span>
      </div>
    </div>
    <div class="foot-bottom"><span>Copyright © 2018 NORVANTA, All Rights Reserved</span><span>Privacy Policy - Terms &amp; Conditions</span></div>
  </footer>
</main>

<!-- Mobile layout -->
<main class="page mobile">
  <header class="m-header">
    <span class="burger"></span><span class="logo">Norvanta</span><span class="account">Login | <b>Register</b></span>
  </header>
  <section class="m-hero">
    <div class="photo hero-photo" role="img" aria-label="Businessman in a suit facing a city skyline"></div>
    <div class="hero-copy"><h1>YOUR GATEWAY</h1><p>TO A BETTER FUTURE</p></div>
  </section>
  <section class="m-search blue-band">
    <div class="field">Job title, Keywords or Company name</div>
    <div class="field">City, Province or region</div>
    <p class="browse">Or browse jobs offer by <span>Category</span></p>
    <div class="search-go"><svg width="4" height="4"><use href="#i-lens"/></svg></div>
  </section>
  <section class="m-jobs">
    <h2 class="section-title">Feature <em>Jobs</em></h2>
    <article class="m-job"><h3>Job Title</h3><p class="role">Scrum Master</p>
      <div class="job-meta"><span>Part-Time</span><span>China</span><span>Up to $55000</span><span>8 AM to 5 PM</span></div>
      <div class="acts"><span class="btn btn-grey">Full Detail</span><span class="btn btn-blue">Quick Inquiry</span></div></article>
    <article class="m-job"><h3>Job Title</h3><p class="role">Scrum Master</p>
      <div class="job-meta"><span>Full-Time</span><span>USA</span><span>Up to $55000</span><span>8 AM to 5 PM</span></div>
      <div class="acts"><span class="btn btn-blue">Full Detail</span><span class="btn btn-blue">Quick Inquiry</span></div></article>
    <article class="m-job"><h3>Job Title</h3><p class="role">Scrum Master</p>
      <div class="job-meta"><span>Full-Time</span><span>USA</span><span>Up to $30000</span><span>8 AM to 5 PM</span></div>
      <div class="acts"><span class="btn btn-blue">Full Detail</span><span class="btn btn-blue">Quick Inquiry</span></div></article>
    <div class="view-all"><span class="btn btn-blue">View All Jobs</span></div>
  </section>
  <section class="m-about blue-band">
    <h2>ABOUT US</h2>
    <p>Lorem Ipsum is simply dummy text of the printing and typesetting industry. Lorem Ipsum has been the industry's standard dummy text ever since the 1500s, when an unknown printer took a galley of type.</p>
    <span class="btn btn-grey">Read More</span>
  </section>
  <div class="photo office-photo m-photo" role="img" aria-label="Recruiter shaking hands with a smiling candidate in an office"></div>
  <section class="m-how">
    <h2 class="section-title">How we <em>work?</em></h2>
    <div class="m-step"><svg><use href="#i-connect"/></svg><h4>Connect</h4><p>Lorem Ipsum is simply dummy text of the printing and typesetting industry.</p></div>
    <div class="m-step"><svg><use href="#i-analyze"/></svg><h4>Analyze</h4><p>Lorem Ipsum is simply dummy text of the printing and typesetting industry.</p></div>
    <div class="m-step"><svg><use href="#i-search"/></svg><h4>Search</h4><p>Lorem Ipsum is simply dummy text of the printing and typesetting industry.</p></div>
    <div class="m-step"><svg><use href="#i-rank"/></svg><h4>Rank</h4><p>Lorem Ipsum is simply dummy text of the printing and typesetting industry.</p></div>
    <div class="m-step"><svg><use href="#i-deliver"/></svg><h4>Deliver</h4><p>Lorem Ipsum is simply dummy text of the printing and typesetting industry.</p></div>
  </section>
  <div class="photo desk-photo m-sub-photo" role="img" aria-label="Young woman working on a laptop at a wooden desk"></div>
  <form class="m-subscribe blue-band">
    <h2>SUBSCRIBE</h2>
    <div class="grid2">
      <div class="input">Your name</div><div class="input">Your surname</div>
      <div class="input">Email address</div><div class="input">Phone#</div>
    </div>
    <div class="textarea">Message<span class="upload">Upload Resume</span></div>
    <span class="btn btn-grey">Subscribe</span>
  </form>
  <section class="m-cands">
    <h2 class="section-title">Feature <em>Candidates</em></h2>
    <div class="cand-row">
      <span class="arrow prev"></span>
      <div class="cand"><div class="avatar" role="img" aria-label="Candidate portrait"></div><b>Liam Porter</b><i>Designation</i></div>
      <div class="cand"><div class="avatar" role="img" aria-label="Candidate portrait"></div><b>Noah Grant</b><i>Designation</i></div>
      <div class="cand"><div class="avatar" role="img" aria-label="Candidate portrait"></div><b>Ethan Cole</b><i>Designation</i></div>
      <span class="arrow next"></span>
    </div>
    <span class="btn btn-blue">View All Candidates</span>
  </section>
  <footer class="m-footer">
    <span class="logo">Norvanta</span>
    <p>Lorem Ipsum is simply dummy text of the printing and typesetting industry. Lorem Ipsum has been the industry's standard dummy text ever since the 1500s.</p>
    <div class="socials"><span></span><span></span><span></span><span></span></div>
    <div class="m-links"><div>Quick Links<i></i></div><div>Useful Info..<i></i></div><div>Contact us<i></i></div></div>
    <div class="m-copy">Copyright © 2018 NORVANTA, All Rights Reserved<br>Privacy Policy - Terms &amp; Conditions</div>
  </footer>
</main>

</body>
</html>
```